improvement on my landing page

We are a fansite platform similar to brindlefold.com, quillmarsh.com , tovarenel.com and gleamwick.com. We are aiming to disrupt this space by a much cheaper and advanced platform to help influencers monetise across different tools.

current lander is https://lumorabey.com/

Looking for a modern, clean, feminine , pink. Current style and other competitors list given feel old and this needs to highlight its a cutting edge product replacing them. Designs I like are www.kelvadrop.app for example.

I need a few elaborations from current site on price differences of competitors, icons and more details on features and several other new sections added. Need a form to capture email , name and phone as this is a coming soon page. Can change later as a signup

attached document is how thee site looks, so need to keep the identity

Target Market(s)

influence's, adult

Font styles to use
Sans Serif

Colors
eea4c8
fefafc
ecdaeb

Requirements
Nice to have
• infographics

```html
<!DOCTYPE html>
<html lang="en">
<head>
<meta charset="utf-8">
<title>Lumorabey — Keep 90% of your earnings</title>
<link rel="stylesheet" href="https://fonts.googleapis.com/css2?family=Comfortaa:wght@400;500;700&display=swap">
<style>
:root{
  --pink:#e21b5e;
  --pink-soft:#fcf0f2;
  --plum:#6a1f7a;
  --ink:#333338;
  --muted:#6b6b72;
  --card:#ffffff;
  --field:#f6f6f7;
  --shadow:0 4px 14px rgba(60,20,40,.10);
}
*{box-sizing:border-box;margin:0;padding:0}
html,body{width:1200px;height:4228px;overflow:hidden}
body{position:relative;background:#fff;font-family:"Comfortaa",sans-serif;color:var(--ink)}
.abs{position:absolute}
.backdrop{position:absolute;left:0;top:0}
.accent{color:var(--pink)}

.brand{left:150px;top:30px;display:flex;align-items:center;gap:16px}
.brand-dot{width:72px;height:72px;border-radius:50%;background:var(--ink)}
.brand-name{font-size:40px;color:var(--pink);font-weight:500;letter-spacing:.5px}

.hero-icon{left:150px;top:197px}
.hero-title{left:150px;top:300px;font-size:32px;line-height:46px;font-weight:400;letter-spacing:.4px}
.hero-copy{left:150px;top:420px;width:450px;font-size:15px;line-height:22px;color:var(--ink)}
.hero-copy b{color:var(--pink);font-weight:700}
.btn{display:block;background:var(--pink);color:#fff;border-radius:20px;text-align:center;font-size:15px}
.hero-btn{left:150px;top:525px;width:151px;height:36px;line-height:36px}

.why-mark{left:972px;top:590px;display:flex;align-items:center;gap:10px}
.why-mark span{width:60px;height:60px;border-radius:50%;background:var(--ink)}
.why-title{left:611px;top:705px;font-size:31px;font-weight:400}
.why-copy{left:611px;top:778px;width:445px;font-size:15px;line-height:22px}
.why-copy p+p{margin-top:22px}
.read-more{left:611px;width:440px;top:975px;text-align:right;color:var(--pink);font-size:15px}

.section-title{left:0;width:1200px;text-align:center;font-size:31px;font-weight:400}
.section-title .accent{display:inline-block;border-bottom:3px solid var(--plum);padding-bottom:2px}

.creators{left:150px;top:1233px;display:grid;grid-template-columns:repeat(4,203px);column-gap:29px;row-gap:38px}
.creator{position:relative;height:225px;box-shadow:var(--shadow);overflow:hidden}
.creator .photo{position:absolute;inset:0}
.creator figcaption{position:absolute;left:0;right:0;bottom:0;height:32px;line-height:32px;background:rgba(40,40,48,.62);color:#fff;text-align:center;font-size:15px}

.feature{background:var(--card);box-shadow:var(--shadow);text-align:center;padding:0 14px}
.feature h3{color:var(--pink);font-weight:400;font-size:12.5px;line-height:17px;margin:18px 0 6px}
.feature p{font-size:11.5px;line-height:20px;color:var(--ink)}
.feature svg{margin-top:38px}
.feature.featured{padding:0 18px}
.feature.featured h3{font-size:17px;margin-top:22px}
.feature.featured p{font-size:15px;line-height:20px}

.dots{left:0;width:1200px;display:flex;justify-content:center;gap:14px}
.dots i{width:9px;height:9px;border-radius:50%;border:1.5px solid var(--ink)}
.dots i.on{background:var(--ink)}

.quote{background:var(--card);border-radius:18px;box-shadow:var(--shadow);padding:40px 18px 0}
.quote p{font-size:11px;line-height:17px;color:var(--ink)}
.quote cite{display:block;text-align:right;font-style:normal;font-size:11px;margin-top:12px}
.avatar{border-radius:50%;width:151px;height:151px}

.fee{background:var(--card);box-shadow:var(--shadow);text-align:center}
.fee .mark{width:74px;height:74px;border-radius:50%;margin:52px auto 0;background:var(--pink)}
.fee .name{color:var(--pink);font-size:13px;margin-top:24px}
.fee .rate{font-size:40px;margin-top:30px}
.fee.featured{border:2px solid var(--pink);z-index:2}
.fee.featured .mark{margin-top:38px}
.fee.featured .rate{font-size:44px;margin-top:50px}

.signup{left:263px;top:3543px;width:673px;height:526px;background:#fff;box-shadow:0 4px 18px rgba(60,20,40,.12);text-align:center}
.signup h2{font-weight:400;font-size:33px;margin-top:33px}
.signup .sub{font-size:15px;margin-top:14px;color:var(--ink)}
.signup .field{position:absolute;left:97px;width:479px;height:36px;background:var(--field);border:none;font-family:inherit;font-size:12px;color:#8a8a90;padding-left:20px;text-align:left;line-height:36px;box-shadow:0 1px 3px rgba(0,0,0,.06)}
.signup .submit{position:absolute;left:187px;top:437px;width:300px;height:36px;line-height:36px;font-size:15px}

.footer-links{top:4144px;left:0;width:1200px;display:flex;justify-content:center;gap:72px;font-size:12px;color:var(--muted)}
</style>
</head>
<body>

<svg class="backdrop" width="1200" height="4228" aria-hidden="true">
  <polygon points="1133,0 1200,0 1200,960 0,1232 0,1125" fill="var(--pink-soft)"/>
  <polygon points="1200,1798 1200,2315 0,2488 0,1970" fill="var(--pink-soft)"/>
  <polygon points="1200,2816 1200,3478 0,3478 0,3087" fill="var(--pink-soft)"/>
</svg>

<header class="abs brand">
  <span class="brand-dot"></span>
  <span class="brand-name">LUMORABEY</span>
</header>

<section class="hero">
  <svg class="abs hero-icon" width="80" height="72" viewBox="0 0 80 72" fill="none" stroke="#222" stroke-width="3" stroke-linejoin="round" stroke-linecap="round" aria-hidden="true">
    <circle cx="53" cy="18" r="15"/>
    <path d="M53 9v18M58 12c-2-2-9-2-9 2s9 2 9 6-7 4-9 2"/>
    <rect x="3" y="40" width="12" height="26"/>
    <path d="M15 44h14c4 0 8 4 10 6h12c3 0 3 5 0 5H36M15 62h30l28-16c3-2 1-7-3-5L52 50"/>
  </svg>
  <h1 class="abs hero-title">KEEP <span class="accent">90%</span> OF YOUR<br>EARNINGS. NO HIDDEN FEES.</h1>
  <p class="abs hero-copy">Make more with added revenue streams and features for <b>FREE</b>. Maximise you're your fanbase profits with Lumorabey</p>
  <a class="abs btn hero-btn">Get Started</a>
</section>

<section class="why">
  <div class="abs why-mark"><span></span></div>
  <h2 class="abs why-title">WHY CHOOSE <span class="accent">LUMORABEY</span>?</h2>
  <div class="abs why-copy">
    <p>Receive 90% of your earnings, with no hidden fees or extras AND with fastest payouts. Monetize with monthly subscriptions through private profile feeds and premium social media accounts.</p>
    <p>Private messaging and tipping, premium videos and much more. Start earning more and keeping your profits.</p>
  </div>
  <a class="abs read-more">Read more</a>
</section>

<h2 class="abs section-title" style="top:1132px">OUR <span class="accent">INFLUENCERS</span></h2>
<div class="abs creators">
  <figure class="creator"><div class="photo" role="img" aria-label="Portrait of Elizabeth Williams" style="background:linear-gradient(160deg,#8fc3d8,#b99a80)"></div><figcaption>Elizabeth Williams</figcaption></figure>
  <figure class="creator"><div class="photo" role="img" aria-label="Portrait of Tereso Courtney" style="background:linear-gradient(180deg,#f2f2f2,#a59a94)"></div><figcaption>Tereso Courtney</figcaption></figure>
  <figure class="creator"><div class="photo" role="img" aria-label="Portrait of Beatrice White" style="background:linear-gradient(160deg,#7d8a6e,#d8d2c8)"></div><figcaption>Beatrice White</figcaption></figure>
  <figure class="creator"><div class="photo" role="img" aria-label="Portrait of Robie Quinn" style="background:linear-gradient(180deg,#9fb0be,#a98455)"></div><figcaption>Robie Quinn</figcaption></figure>
  <figure class="creator"><div class="photo" role="img" aria-label="Portrait of Bonnie Carter" style="background:linear-gradient(160deg,#d8d8d8,#7a6a62)"></div><figcaption>Bonnie Carter</figcaption></figure>
  <figure class="creator"><div class="photo" role="img" aria-label="Portrait of Katherine Sparks" style="background:linear-gradient(160deg,#d9366f,#3c4f7a)"></div><figcaption>Katherine Sparks</figcaption></figure>
  <figure class="creator"><div class="photo" role="img" aria-label="Portrait of Emmie Watts" style="background:linear-gradient(120deg,#7e93a8,#f0a030 70%,#d84a7a)"></div><figcaption>Emmie Watts</figcaption></figure>
  <figure class="creator"><div class="photo" role="img" aria-label="Portrait of Bruce Wells" style="background:linear-gradient(160deg,#c8332f,#7a1c1c)"></div><figcaption>Bruce Wells</figcaption></figure>
</div>

<h2 class="abs section-title" style="top:1868px">OUR <span class="accent">FEATURES</span></h2>
<article class="abs feature" style="left:150px;top:1988px;width:157px;height:225px">
  <svg width="38" height="28" viewBox="0 0 38 28" fill="none" stroke="#222" stroke-width="1.8" aria-hidden="true"><rect x="2" y="2" width="34" height="24" rx="2"/><path d="M2 9h34M2 13h34M7 20h12"/><circle cx="29" cy="20" r="2"/></svg>
  <h3>Fastest Payouts</h3><p>You own your content. Take it down whenever you want</p>
</article>
<article class="abs feature" style="left:327px;top:1988px;width:157px;height:225px">
  <svg width="32" height="38" viewBox="0 0 32 38" fill="none" stroke="#222" stroke-width="1.8" aria-hidden="true"><path d="M16 3v3M6 28V17a10 10 0 0 1 20 0v11l3 4H3z"/><path d="M12 33a4 4 0 0 0 8 0"/></svg>
  <h3>Instant Notifications</h3><p>Never miss a beat. Get custom &amp; instant email updates</p>
</article>
<article class="abs feature featured" style="left:502px;top:1970px;width:196px;height:263px">
  <svg width="52" height="50" viewBox="0 0 52 50" fill="none" stroke="#222" stroke-width="2" aria-hidden="true"><rect x="12" y="20" width="28" height="24" rx="3"/><path d="M18 20v-6a8 8 0 0 1 16 0v6"/><circle cx="26" cy="32" r="3"/></svg>
  <h3>Private Snapline</h3><p>Easily sell private snapline acces and monitor subscriptions</p>
</article>
<article class="abs feature" style="left:716px;top:1988px;width:157px;height:225px">
  <svg width="38" height="34" viewBox="0 0 38 34" fill="none" stroke="#222" stroke-width="1.8" aria-hidden="true"><path d="M2 32h34M6 32V22h5v10M15 32V18h5v14M24 32V14h5v14M33 32V8"/><path d="M4 16l9-7 8 4 12-10"/></svg>
  <h3>Inteligent Business Data</h3><p>Easily monitor your business and learn from intuitive data</p>
</article>
<article class="abs feature" style="left:892px;top:1988px;width:157px;height:225px">
  <svg width="40" height="38" viewBox="0 0 40 38" fill="none" stroke="#222" stroke-width="1.8" aria-hidden="true"><path d="M20 3a16 16 0 1 1-9 29l-7 3 2-7A16 16 0 0 1 20 3z"/><circle cx="13" cy="19" r="1.4" fill="#222"/><circle cx="20" cy="19" r="1.4" fill="#222"/><circle cx="27" cy="19" r="1.4" fill="#222"/></svg>
  <h3>Private Messaging</h3><p>Engage with your fans on a personal level. Your choice</p>
</article>
<div class="abs dots" style="top:2275px"><i class="on"></i><i></i><i></i></div>

<h2 class="abs section-title" style="top:2426px">OUR <span class="accent">TESTIMONIALS</span></h2>
<article class="abs quote" style="left:150px;top:2647px;width:262px;height:151px">
  <p>"Lorem ipsum dolor sit amet, consectetur adipiscing elit, sed do eiusmod tempor incididunt ut labore et dolore magna aliqua."</p><cite>John Smith</cite>
</article>
<div class="abs avatar" role="img" aria-label="Photo of John Smith" style="left:206px;top:2529px;background:radial-gradient(circle at 50% 60%,#e0b79a,#5a6470)"></div>
<article class="abs quote" style="left:468px;top:2647px;width:262px;height:151px">
  <p>"Lorem ipsum dolor sit amet, consectetur adipiscing elit, sed do eiusmod tempor incididunt ut labore et dolore magna aliqua."</p><cite>Alexandra Milles</cite>
</article>
<div class="abs avatar" role="img" aria-label="Photo of Alexandra Milles" style="left:524px;top:2529px;background:radial-gradient(circle at 50% 55%,#d9a88a,#3a2a22)"></div>
<article class="abs quote" style="left:788px;top:2647px;width:262px;height:151px">
  <p>"Lorem ipsum dolor sit amet, consectetur adipiscing elit, sed do eiusmod tempor incididunt ut labore et dolore magna aliqua."</p><cite>Jules Steen</cite>
</article>
<div class="abs avatar" role="img" aria-label="Photo of Jules Steen" style="left:844px;top:2529px;background:radial-gradient(circle at 50% 55%,#f0c6b0,#8cc0e0 60%,#e27aa8)"></div>
<div class="abs dots" style="top:2843px"><i class="on"></i><i></i><i></i></div>

<h2 class="abs section-title" style="top:2991px">COMPETITORS <span class="accent">FEES</span></h2>
<article class="abs fee" style="left:150px;top:3113px;width:171px;height:263px"><div class="mark"></div><div class="name">Quillmarsh</div><div class="rate">20%</div></article>
<article class="abs fee" style="left:322px;top:3113px;width:171px;height:263px"><div class="mark"></div><div class="name">Brindlefold</div><div class="rate">15%</div></article>
<article class="abs fee featured" style="left:493px;top:3093px;width:214px;height:303px"><div class="mark"></div><div class="name">LUMORABEY</div><div class="rate">10%</div></article>
<article class="abs fee" style="left:708px;top:3113px;width:171px;height:263px"><div class="mark"></div><div class="name">Gleamwick</div><div class="rate">35%</div></article>
<article class="abs fee" style="left:880px;top:3113px;width:171px;height:263px"><div class="mark"></div><div class="name">Tovarenel</div><div class="rate">43%</div></article>

<form class="abs signup">
  <h2>CREATE YOUR <span class="accent">FREE</span> ACCOUNT</h2>
  <p class="sub">It only takes a few seconds. No credit card required.</p>
  <div class="field" style="top:145px">Username</div>
  <div class="field" style="top:212px">Email</div>
  <div class="field" style="top:279px">Password</div>
  <div class="field" style="top:346px">Confirm Password</div>
  <a class="btn submit">Get Started</a>
</form>

<nav class="abs footer-links"><a>Privacy</a><a>Terms &amp; Conditions</a></nav>

</body>
</html>
```